Landlord Handbook for real estate agency clients

We are a boutique Real Estate Agency that specializes in Property Management (Rentals) Located on Sydney's Northern Beaches.

We are putting together a property owners handbook that informs them about being a landlord, setting up their property for rent, local legislation on leasing properties, the services we offer and what makes us a great choice to manage their property.
Ultimately this is designed to answer new landlords FAQs and sell our agency as the best choice for them.

We want this handbook to be simple, clear and styled to match our existing website. wwww.keystonehavenrealty.com.au

We have supplied some images, screen shots of our Landlord Portal service offered. All words and index are provided in the word.doc
The services we want to feature are:
Our Landlord Portal
Our Service Guarantee
Quality Tenant Database
6 Month Property Reports

I would like the brochure to be around 16-20 A4 pages with some of the images provided and/or any other images you would like to add.

An example of a similar owners handbook can be found here: http://www.vexor.com.au/marlow_tebbit_poh/
But I would like something a little more modern and matched to our website design.

I would like a print ready PDF version of document as well as an editable Photoshop copy and AI copy.

Thank you and I look forward t your designs!
Gus.

Target Market(s)

30-65YO Men and women that own investment properties on Sydney's Northern Beaches

Industry/Entity Type

Real Estate

Font styles to use
Serif

Requirements
Must have
• Must use one of the Town house images provided on the front cover to match our website www.keystonehavenrealty.com.au
• Index of details at the start.
• Use one or all of our screen shot images of the Landlord Portal to promote this feature within the landlord portal description in content.
Should not have
• Any images of foreign currency, landscapes or houses. We are based in Sydney Australia on the beach so we want to keep it local and use Australian images, currency, landscapes and houses.

```html
<!DOCTYPE html>
<html lang="en">
<head>
<meta charset="utf-8">
<title>Keystone Haven Realty – Landlord Handbook, Section 1</title>
<link rel="stylesheet" href="https://fonts.googleapis.com/css2?family=Oswald:wght@500;600&family=Montserrat:wght@700;800&family=Roboto+Slab:wght@300;400&display=swap">
<style>
  :root {
    --backdrop: #a3a3a3;
    --brand-blue: #0f6d96;
    --brand-blue-dark: #0b5678;
    --white: #ffffff;
    --body-text: #d7dde3;
    --sky-top: #2f6f98;
    --sky-mid: #8fb9cf;
    --sea-deep: #1f5d86;
    --sea-shallow: #4f9a8e;
    --night-top: #15191d;
    --night-mid: #1f2a33;
    --pier-tone: #4f6f82;
  }
  * { box-sizing: border-box; margin: 0; padding: 0; }
  html, body { width: 1200px; height: 978px; overflow: hidden; background: var(--backdrop); }

  .spread {
    position: absolute; left: 127px; top: 135px;
    width: 961px; height: 707px;
    display: flex;
    box-shadow: 0 6px 18px rgba(0,0,0,.25);
  }
  .page { position: relative; height: 100%; overflow: hidden; }
  .page--left { width: 479px; }
  .page--right { width: 482px; }

  .photo { position: absolute; inset: 0; }
  .photo--coast {
    background: linear-gradient(180deg, var(--sky-top) 0%, var(--sky-mid) 30%, var(--sea-deep) 36%, #2a6f8c 55%, var(--sea-shallow) 78%, #2f7a6c 100%);
  }
  .photo--waterfront {
    background: linear-gradient(180deg, var(--night-top) 0%, var(--night-mid) 45%, #33495a 68%, var(--pier-tone) 85%, #6a8796 100%);
  }

  .brand-name {
    position: absolute; left: 100px; top: 68px;
    font-family: "Montserrat", sans-serif; font-weight: 700;
    font-size: 27px; letter-spacing: .5px; color: var(--white);
  }

  .section-number {
    position: absolute; left: 24px; top: 440px;
    font-family: "Oswald", sans-serif; font-weight: 600;
    font-size: 52px; line-height: 1; color: #f1f1f1;
  }
  .section-banner {
    position: absolute; left: 0; top: 511px;
    width: 345px; height: 60px;
    background: var(--brand-blue);
    clip-path: polygon(0 0, 100% 0, 94% 100%, 0 100%);
  }
  .section-banner span {
    position: absolute; left: 20px; top: 15px;
    font-family: "Oswald", sans-serif; font-weight: 500;
    font-size: 21px; color: var(--white);
  }

  .page-footer {
    position: absolute; left: 0; right: 0; bottom: 0; height: 32px;
    background: var(--brand-blue);
    font-family: "Roboto Slab", serif; font-weight: 400;
    font-size: 14px; color: var(--white);
    text-align: center; line-height: 32px;
  }
  .page--left .page-footer { padding-left: 20px; }
  .page-footer b { font-weight: 700; }

  .content { position: absolute; left: 18px; right: 12px; top: 22px; }
  .content-title {
    font-family: "Oswald", sans-serif; font-weight: 600;
    font-size: 22px; color: var(--white); text-align: center;
    margin-bottom: 14px;
  }
  .topic-heading {
    font-family: "Montserrat", sans-serif; font-weight: 700;
    font-size: 14.5px; letter-spacing: .4px; color: var(--white);
    margin: 12px 0 12px;
  }
  .topic-question {
    font-family: "Montserrat", sans-serif; font-weight: 700;
    font-size: 13px; color: var(--white); margin-bottom: 12px;
  }
  .topic-body p {
    font-family: "Roboto Slab", serif; font-weight: 300;
    font-size: 10.2px; line-height: 12.6px; color: var(--body-text);
  }
  .topic--marketing .topic-body { margin-bottom: 28px; }
</style>
</head>
<body>
  <div class="spread">
    <section class="page page--left">
      <div class="photo photo--coast" role="img" aria-label="Photograph of a rock pool on the ocean shore with a sculpture and blue sky"></div>
      <div class="brand-name">KEYSTONE HAVEN</div>
      <h1 class="section-number">SECTION 1:</h1>
      <div class="section-banner"><span>COMMON QUESTIONS AND DETAILS:</span></div>
      <footer class="page-footer">www.<b>keystonehavenrealty</b>.com.au</footer>
    </section>

    <section class="page page--right">
      <div class="photo photo--waterfront" role="img" aria-label="Darkened photograph of a waterfront promenade with umbrellas"></div>
      <div class="content">
        <h2 class="content-title">COMMON QUESTIONS AND DETAILS:</h2>

        <article class="topic">
          <h3 class="topic-heading">MAXIMISING YOUR PROPERTY’S RETURN</h3>
          <div class="topic-body">
            <p>We ensure your property is bringing in the strongest return possible by minimizing risk, using proven marketing strategies and being able to shortlist the most reliable tenants for you to select from.</p>
            <p>We have an incredibly low vacancy rate. Built through a strong pre-screened tenant database to market your property to, quick-to-act property managers and creating tenancy agreements that end in strong rental seasons, making it easier to re-tenant your property if necessary.</p>
            <p>Providing you with the best tenants possible paying the best possible rent and minimizing any potential vacancy at your property.</p>
          </div>
        </article>

        <article class="topic topic--marketing">
          <h3 class="topic-heading">MARKETING YOUR PROPERTY</h3>
          <div class="topic-body">
            <p>When listing your property we take high quality pictures, advertise on multiple listing sites including Leasehub.com.au, Rentwise.com.au, our website, our tenant databases, corporate re-locaters and even social media groups.</p>
            <p>High quality leasing signage is used out the front of the upcoming property.</p>
            <p>We have two openings per week Saturday and Wednesday and each opening goes for 30min (twice as long as our competitors).</p>
            <p>We also ensure we are available to take people through for private viewings</p>
          </div>
        </article>

        <article class="topic">
          <h3 class="topic-heading">SELECTING THE BEST TENANT</h3>
          <h4 class="topic-question">So how do we get the best tenant for your property?</h4>
          <div class="topic-body">
            <p>After extensive marketing of your property through multiple media formats. We will receive detailed applications from prospective tenants.</p>
            <p>These applicants are then screened, background checked, employment checked and run through the most up to date digital tenancy databases to ensure they are capable of servicing rent and have no black listed tenancy history.</p>
            <p>We also ensure your quality tenant gets the attention they deserve and reward them for being great. A great tenant is worth their weight in gold and we ensure they want to continue leasing your property.</p>
          </div>
        </article>

        <article class="topic">
          <h3 class="topic-heading">TAKING A BOND</h3>
          <div class="topic-body">
            <p>Current regulations stipulate that the bond can be no more than 4 weeks rent based on the initial tenancy agreement. We use the latest technology with the Tenancy Office’s Bond Lodgement Online – which means we can secure and lodge the bond with the Tenancy Office fast – ensuring you can get your tenant in fast and securely.</p>
          </div>
        </article>
      </div>
      <footer class="page-footer">www.<b>keystonehavenrealty</b>.com.au</footer>
    </section>
  </div>
</body>
</html>
```